Redesign responsive website and logo for webshop platform

Redesign our applications old website with a new clean, crisp modern looking style that is responsive.

Our application is a cloud based, free ecommerce platform that lets users set up their own webshops within minutes. (Similar to Bramvik https://bramvik.example/l/sell)

Our old website: http://sv.kelporia.example/

I need redesigned HTML + CSS for the following three pages:
* Landing Page:
(Old page: http://sv.kelporia.example/)
I have attached a mockup of a proposed layout/structure for the landing page.
- Pricing comparision/features page
(Old page http://sv.kelporia.example/t/funktioner)
- Generic "article" page:
(Old page http://sv.kelporia.example/d/redigerasida)

The pages must responsive using HTML 5/CSS 3 (I prefer Bootstrap 3 if possible).

I also need a redesign of the logotype.

If you have any questions don't hesitate to ask and we will provide whatever is needed to you.

Logo Text

Kelporia

Coding

Coded - Design and coding required

Number of Pages Required

3 page

Font styles to use
Serif
Sans Serif

```html
<!DOCTYPE html>
<html lang="sv">
<head>
<meta charset="utf-8">
<title>Kelporia – Starta en gratis webshop</title>
<link rel="stylesheet" href="https://fonts.googleapis.com/css2?family=Questrial&display=swap">
<style>
  :root {
    --brand-blue: #1a5faa;
    --sky: #36a6dc;
    --page-bg: #f4f4f4;
    --white: #ffffff;
    --ink: #222222;
    --muted: #555555;
    --line: #e2e2e2;
    --form-dark: #17232b;
    --form-line: #3a4a54;
  }
  * { box-sizing: border-box; margin: 0; padding: 0; }
  html, body { width: 672px; height: 1200px; overflow: hidden; }
  body {
    position: relative;
    background: var(--page-bg);
    font-family: "Questrial", "Century Gothic", sans-serif;
    color: var(--ink);
  }
  .abs { position: absolute; }

  /* Header */
  .site-header { left: 0; top: 0; width: 672px; height: 40px; background: var(--white); }
  .contact-item { top: 15px; font-size: 6.5px; color: var(--muted); display: flex; align-items: center; gap: 4px; white-space: nowrap; }
  .contact-item .dot { width: 5px; height: 5px; background: var(--sky); border-radius: 1px; flex: none; }
  .brand { left: 272px; top: 10px; display: flex; align-items: center; gap: 6px; }
  .brand .mark { width: 14px; height: 14px; border-radius: 50%; background: var(--sky); }
  .brand .name { font-size: 15px; color: var(--brand-blue); letter-spacing: 0.5px; }
  .btn-small {
    top: 13px; height: 15px; padding: 0 5px; font-size: 6.5px; color: var(--white);
    background: var(--sky); line-height: 15px; border-bottom: 1px solid #1d7fb2; white-space: nowrap;
  }

  /* Hero */
  .hero-photo {
    left: 0; top: 40px; width: 672px; height: 195px;
    background: linear-gradient(90deg, #d9d4cf 0%, #cfc7bf 35%, #e6d8cc 55%, #d8cfc8 80%, #c9c3c2 100%);
  }
  .hero-card {
    left: 79px; top: 100px; width: 193px; height: 86px;
    background: var(--brand-blue); color: var(--white); text-align: center; padding: 11px 6px 0;
  }
  .hero-card h1 { font-size: 10.5px; font-weight: normal; margin-bottom: 3px; }
  .hero-card p { font-size: 7.5px; line-height: 13px; }

  /* Features */
  .feature {
    width: 240px; height: 83px; background: var(--white); border: 1px solid var(--line);
    text-align: center; padding-top: 10px;
  }
  .feature h2 { font-size: 10.5px; font-weight: normal; margin-bottom: 11px; }
  .feature p { font-size: 5.8px; line-height: 13px; color: var(--muted); padding: 0 36px; }

  /* Slider */
  .slider { left: 0; top: 552px; width: 672px; height: 195px; background: var(--brand-blue); color: var(--white); }
  .slider h3 { position: absolute; left: 80px; top: 15px; font-size: 10.5px; font-weight: normal; }
  .slider .copy { position: absolute; left: 80px; top: 44px; width: 360px; font-size: 7.3px; line-height: 13px; }
  .slider .copy p { margin-bottom: 13px; }
  .slider .back-link { position: absolute; left: 80px; top: 171px; font-size: 8px; color: var(--sky); }
  .shot { background: linear-gradient(160deg, #ffffff, #dfe6ee); border: 2px solid var(--white); }

  /* Ticket form */
  .ticket-frame { left: 178px; top: 770px; width: 296px; height: 212px; background: var(--sky); }
  .ticket { left: 187px; top: 777px; width: 278px; height: 197px; background: var(--form-dark); border: 1px solid #0e161b; }
  .ticket h4 { position: absolute; left: 9px; top: 16px; font-size: 9.5px; font-weight: normal; color: var(--sky); }
  .field-label { font-size: 5.8px; color: var(--white); }
  .field-line { height: 1px; background: var(--form-line); }
  .btn-send { height: 18px; padding: 0 11px; background: var(--brand-blue); color: var(--white); font-size: 7.5px; line-height: 18px; }

  /* Footer */
  .footer-photo {
    left: 0; top: 1005px; width: 672px; height: 195px;
    background: linear-gradient(90deg, #1a5faa 0%, #1e63ad 40%, #4d7fb8 70%, #6d8fb4 100%);
  }
  .footer-title { left: 79px; top: 1014px; font-size: 12.5px; color: var(--white); white-space: nowrap; }
  .tab { top: 1037px; height: 16px; padding: 0 6px; font-size: 7px; line-height: 14px; color: var(--white); border: 1px solid var(--white); white-space: nowrap; }
  .tab.active { background: var(--sky); border-color: var(--sky); }
  .f-label { font-size: 5.8px; color: var(--white); white-space: nowrap; }
  .f-line { height: 1px; background: rgba(255,255,255,0.3); }
  .btn-footer { left: 79px; top: 1136px; height: 18px; padding: 0 11px; background: var(--sky); color: var(--white); font-size: 7.5px; line-height: 18px; }
  .footer-rule { left: 79px; top: 1178px; width: 494px; height: 1px; background: rgba(255,255,255,0.45); }
  .copyright { left: 0; top: 1184px; width: 672px; text-align: center; font-size: 5.8px; color: var(--white); }
</style>
</head>
<body>

<header class="site-header abs">
  <div class="contact-item abs" style="left:79px"><span class="dot"></span>info@kelporia.example</div>
  <div class="contact-item abs" style="left:170px"><span class="dot"></span>Kelporia på Flockr</div>
  <div class="brand abs"><span class="mark"></span><span class="name">KELPORIA</span></div>
  <div class="btn-small abs" style="left:502px">SIGN IN</div>
  <div class="btn-small abs" style="left:540px">LOG IN</div>
</header>

<div class="hero-photo abs" role="img" aria-label="Foto: leende kvinna med mobiltelefon och shoppingkassar i en ljus galleria"></div>
<div class="hero-card abs">
  <h1>Starta en gratis webshop</h1>
  <p>Kelporia är en tjänst som låter dig starta en komplett internetbutik. Tjänsten är gratis och har allt som krävs för att du ska komma igång med din verksamhet och sälja produkter online.</p>
</div>

<section>
  <div class="feature abs" style="left:80px;top:257px"><h2>Kom igång på 5 minuter</h2><p>Att starta en ebutik med Kelporia tar inte mer än 5 minuter. Skapa ett konto för att komma igång. Ingenting behöver installeras på din dator.</p></div>
  <div class="feature abs" style="left:332px;top:257px"><h2>Skapa en gratis webbutik</h2><p>Kelporia är en gratis tjänst. Tjänsten har varken månadskostnader eller transaktionsavgifter på det du säljer.</p></div>
  <div class="feature abs" style="left:80px;top:352px"><h2>Intuitivt användargränssnitt</h2><p>Det går snabb att lägga till nya produkter. Organisera produkter genom att dra och släppa.</p></div>
  <div class="feature abs" style="left:332px;top:352px"><h2>Sökmotoroptimerad</h2><p>Kelporia är genomgående skapat med sökmotoroptimering som en fokuspunkt</p></div>
  <div class="feature abs" style="left:80px;top:448px"><h2>Designa din webshop</h2><p>Välj bland färdiga utseendemallar eller skapa din egen grafiska profil med ett par klick.</p></div>
  <div class="feature abs" style="left:332px;top:448px"><h2>Smart Dashboard</h2><p>På startsidan i din webbutik får du en överblick om senast inkomna ordrar, analys och statistik om försäljningar mm</p></div>
</section>

<section class="slider abs">
  <h3>Enkel webshop design</h3>
  <div class="copy">
    <p>Det är viktigt att din webbutik har ett utseende och helhetsintryck som stämmer väl överrens med din verksamhet/varumärke.</p>
    <p>Med Kelporia behövs varken CSS/HTML-kunskaper eller anlita en designer för att skapa en snygg layout. Det är enkelt att själva anpassa webshopens färger och layout för att återspela ditt företags grafiska profil.</p>
    <p>Förutom att ladda upp din egen logotyp har Kelporia flera färdiga layouter/grafiska teman att välja mellan. När du valt en layout kan du anpassa denna genom att ändra färger och stil med ett intuitivt användargränssnitt där det bara krävs ett par klick för att se resultat direkt.</p>
  </div>
  <div class="back-link">Tillbaks Till Funktioner &#8594;</div>
  <svg class="abs" style="left:48px;top:82px" width="12" height="16" viewBox="0 0 12 16"><path d="M9 2 L3 8 L9 14" stroke="#fff" stroke-width="2.5" fill="none"/></svg>
  <svg class="abs" style="left:590px;top:82px" width="12" height="16" viewBox="0 0 12 16"><path d="M3 2 L9 8 L3 14" stroke="#fff" stroke-width="2.5" fill="none"/></svg>
  <div class="shot abs" role="img" aria-label="Skärmbild av webshopens produktsida" style="left:488px;top:16px;width:82px;height:62px;transform:rotate(12deg)"></div>
  <div class="shot abs" role="img" aria-label="Skärmbild av färgverktyget i webshopens designläge" style="left:486px;top:100px;width:80px;height:80px;transform:rotate(5deg)"></div>
</section>

<div class="ticket-frame abs"></div>
<form class="ticket abs">
  <h4>Skapa ett nytt ärende</h4>
  <div class="field-label abs" style="left:9px;top:41px">Ämne</div>
  <div class="field-line abs" style="left:9px;top:51px;width:258px"></div>
  <div class="field-label abs" style="left:9px;top:63px">Meddelande</div>
  <div class="field-line abs" style="left:9px;top:116px;width:258px"></div>
  <div class="field-label abs" style="left:9px;top:126px">Din-e-Post</div>
  <div class="field-line abs" style="left:9px;top:138px;width:124px"></div>
  <div class="field-label abs" style="left:142px;top:126px">Ditt Namn</div>
  <div class="field-line abs" style="left:142px;top:138px;width:125px"></div>
  <div class="btn-send abs" style="left:9px;top:162px">SKICKA</div>
</form>

<footer>
  <div class="footer-photo abs" role="img" aria-label="Foto: bärbar dator på ett kafébord som visar webbplatsens startsida"></div>
  <div class="footer-title abs">Discover Kelporia.Start Your Shop Today.</div>
  <div class="tab active abs" style="left:80px">Frågor</div>
  <div class="tab abs" style="left:129px">Förslag</div>
  <div class="tab abs" style="left:178px">Problem</div>
  <div class="tab abs" style="left:228px">Beröm</div>
  <div class="f-label abs" style="left:79px;top:1060px">Beskriv Kortfattat Din Fråg</div>
  <div class="f-line abs" style="left:79px;top:1070px;width:240px"></div>
  <div class="f-label abs" style="left:79px;top:1078px">Gen En Längre Beskrivning Av Ärendet</div>
  <div class="f-line abs" style="left:79px;top:1100px;width:240px"></div>
  <div class="f-label abs" style="left:79px;top:1108px">Din-e-Post</div>
  <div class="f-line abs" style="left:79px;top:1122px;width:106px"></div>
  <div class="f-label abs" style="left:213px;top:1108px">Ditt Namn</div>
  <div class="f-line abs" style="left:213px;top:1122px;width:106px"></div>
  <div class="btn-footer abs">SKICKA</div>
  <div class="footer-rule abs"></div>
  <div class="copyright abs">© 2016 Varnholt | Support | Dokumentation</div>
</footer>

</body>
</html>
```